Clone http://www.pebbledeskwriter.com/ (fully functioning WordPress website - not just design)

1) Clone or recreate http://www.pebbledeskwriter.com/ in Wordpress with WooCommerece plugin
2) Connect to our Existing Quendo Account
3) Make site-wide text only changes that we provide you when site is complete.

We will provide all the graphics according to your size requirements.

Cash awarded to the closest copy of http://www.pebbledeskwriter.com/

Target Market(s)

WordPress developer

Number of Pages Required

5+ page

Font styles to use
Sans Serif

Colors
abd037
cadf82
eaf2ce

Requirements
Must have
• Fully functioning website.

```html
<!DOCTYPE html>
<html lang="en">
<head>
<meta charset="utf-8">
<title>Pebbledesk Writer – Easy, Online Mail Merge</title>
<link href="https://fonts.googleapis.com/css2?family=Lato:wght@400;700;900&display=swap" rel="stylesheet">
<style>
:root{
  --green:#abd037;
  --green-mid:#cadf82;
  --green-pale:#eaf2ce;
  --ink:#3a3a3a;
  --muted:#7a7a7a;
  --white:#ffffff;
  --grey-bg:#ececec;
  --footer:#3b3b3b;
  --footer-text:#c9c9c9;
}
*{box-sizing:border-box;margin:0;padding:0}
html,body{width:1200px;height:3822px;overflow:hidden}
body{font-family:'Lato',Arial,sans-serif;color:var(--ink);background:var(--white);position:relative}
section,header,footer{position:absolute;left:0;width:1200px}
.abs{position:absolute}
.center{text-align:center}

/* header */
.site-header{top:0;height:70px}
.brand{left:70px;top:8px;width:220px;text-align:center}
.brand-mark{width:26px;height:26px;border-radius:50%;background:var(--green);margin:0 auto 6px}
.brand-name{font-size:17px;font-weight:700;color:#444}
.main-nav{left:527px;top:38px;display:flex;gap:22px;font-size:13px}
.main-nav a{color:#555;text-decoration:none}
.main-nav a.active{color:var(--green)}
.nav-divider{left:805px;top:32px;width:1px;height:26px;background:#ddd}
.social{top:36px;width:24px;height:24px;border-radius:50%;background:var(--green)}
.login{left:985px;top:40px;font-size:13px;color:#555}
.register{left:1042px;top:35px;width:72px;height:24px;background:var(--green);color:#fff;font-size:11px;text-align:center;line-height:24px}
.nav-divider2{left:960px;top:32px;width:1px;height:26px;background:#ddd}

/* hero */
.hero{top:70px;height:452px}
.hero-art{left:120px;top:20px;width:900px;height:432px;background:linear-gradient(180deg,#ffffff 0%,var(--green-pale) 60%,var(--green-mid) 100%)}
.hero-title{left:398px;top:162px;width:404px;font-size:31px;font-weight:700;color:var(--green)}
.hero-btn{left:528px;top:215px;width:144px;height:34px;background:var(--green);color:#fff;font-size:14px;font-weight:700;line-height:34px}
.hero-sub{left:398px;top:262px;width:404px;font-size:11px;color:#666}
.slider-dots{left:1106px;top:190px;width:14px}
.dot{width:12px;height:12px;border-radius:50%;background:var(--green);margin-bottom:13px}
.dot.ring{background:#fff;border:2px solid var(--green)}

.intro-band{top:522px;height:108px;background:var(--green);color:#fff;text-align:center}
.intro-band h2{font-size:19px;font-weight:700;margin-top:24px}
.intro-band p{font-size:11px;width:560px;margin:10px auto 0;line-height:16px}

/* features */
.features{top:630px;height:320px}
.feature{top:38px;width:240px;text-align:center}
.feature-icon{width:140px;height:140px;border-radius:50%;background:var(--green-pale);margin:0 auto;display:flex;align-items:center;justify-content:center}
.feature h3{font-size:17px;color:var(--green);font-weight:700;margin-top:28px}
.feature hr{width:60px;border:0;border-top:2px solid var(--green);margin:8px auto 12px}
.feature p{font-size:11px;color:var(--muted);line-height:16px;width:175px;margin:0 auto}
.feature .rule{width:175px;height:1px;background:var(--green);margin:14px auto 0}

/* steps */
.steps{top:950px;height:367px}
.steps-art{left:270px;top:20px;width:318px;height:320px;background:radial-gradient(circle at 50% 45%,var(--green-pale),#f2f6e6 70%,#fff)}
.steps h2{left:612px;top:64px;font-size:30px;font-weight:700;color:var(--green);line-height:34px;width:400px}
.steps .lead{left:612px;top:140px;font-size:11px;color:var(--muted)}
.step{left:612px;width:380px;display:flex;gap:14px}
.step-num{width:34px;height:34px;border-radius:50%;border:2px solid var(--green);color:var(--green);font-weight:700;font-size:15px;text-align:center;line-height:30px;flex:none}
.step h4{font-size:14px;color:var(--green);font-weight:700}
.step p{font-size:11px;color:#555;margin-top:3px}

/* pricing */
.pricing{top:1317px;height:459px;background:var(--grey-bg)}
.pricing h2{top:48px;left:0;width:1200px;font-size:26px;color:var(--green);font-weight:700}
.plan{width:237px;text-align:center}
.plan-free{left:357px;top:123px;height:285px;background:#fff}
.plan-paid{left:596px;top:117px;height:291px;background:var(--green);color:#fff}
.plan-label{height:40px;line-height:40px;font-size:13px;font-weight:700;letter-spacing:.5px}
.plan-free .plan-label{color:var(--green);border-bottom:1px solid #e5e5e5}
.plan-paid .plan-label{border-bottom:1px solid rgba(255,255,255,.5)}
.plan-price{font-size:46px;font-weight:700;margin-top:22px;line-height:50px}
.plan-free .plan-price{color:var(--green)}
.plan-price sup{font-size:22px;vertical-align:top;line-height:30px}
.plan-sub{font-size:11px;margin-bottom:12px}
.plan-detail{font-size:11px;line-height:15px;color:#444}
.plan-paid .plan-detail{color:#fff}
.plan-btn{position:absolute;left:42px;bottom:28px;width:150px;height:38px;line-height:38px;font-size:13px;font-weight:700}
.plan-free .plan-btn{background:var(--green);color:#fff}
.plan-paid .plan-btn{background:#fff;color:var(--green)}

/* team */
.team{top:1776px;height:594px}
.team h2{top:40px;left:0;width:1200px;font-size:26px;color:var(--green);font-weight:700}
.member{top:122px;width:260px;text-align:center}
.member-photo{width:199px;height:199px;border-radius:50%;background:linear-gradient(135deg,#d6d6d6,#6e6e6e);margin:0 auto}
.member-badge{width:89px;height:89px;border-radius:50%;background:var(--green);border:5px solid #fff;margin:-44px auto 0;display:flex;align-items:center;justify-content:center;position:relative}
.member h3{font-size:18px;color:var(--green);font-weight:700;margin-top:8px}
.member p{font-size:11px;color:var(--muted);line-height:15px;width:220px;margin:6px auto 0}
.team-dots{top:510px;left:578px;display:flex;gap:14px}
.team-dots span{width:10px;height:10px;border-radius:50%;background:var(--green)}
.team-dots span.ring{background:#fff;border:2px solid var(--green)}

/* testimonial */
.testimonial{top:2421px;height:275px;background:var(--green);color:#fff;text-align:center}
.avatar{left:550px;top:-51px;width:102px;height:102px;border-radius:50%;background:linear-gradient(135deg,#c9c2bb,#7d6e66);border:4px solid #fff}
.testimonial .kicker{top:72px;left:0;width:1200px;font-size:13px}
.testimonial blockquote{top:112px;left:240px;width:720px;font-size:18px;font-weight:700;line-height:28px}
.testimonial .author{top:228px;left:0;width:1200px;font-size:11px;font-style:normal;letter-spacing:1px;text-align:center}
.testimonial .slider-dots{top:93px}
.testimonial .dot{background:#fff}
.testimonial .dot.ring{background:var(--green);border-color:#fff}

/* clients */
.clients{top:2696px;height:311px}
.clients h2{top:48px;left:0;width:1200px;font-size:26px;color:var(--green);font-weight:700}
.clients p{top:100px;left:0;width:1200px;font-size:11px;color:var(--muted);line-height:16px}
.client-row{top:178px;left:200px;width:800px;display:flex;justify-content:space-between;align-items:center}
.client{display:flex;align-items:center;gap:6px;font-size:15px;font-weight:700;color:#555}
.client i{width:16px;height:16px;border-radius:50%;background:var(--green);display:block}

/* contact */
.contact{top:3007px;height:504px}
.contact-form{left:0;top:0;width:581px;height:504px;background:var(--green)}
.contact-form h2{left:69px;top:82px;font-size:30px;color:#fff;font-weight:700}
.contact-form hr{position:absolute;left:69px;top:128px;width:80px;border:0;border-top:2px solid #fff}
.field{left:69px;width:425px;height:26px;background:#fff;font-size:9px;color:#777;padding:7px 6px}
.field.message{height:115px}
.clear{left:440px;top:414px;font-size:10px;color:#fff;display:flex;align-items:center;gap:6px}
.clear span{width:16px;height:16px;border-radius:50%;border:2px solid #fff;display:inline-block}
.send-btn{left:69px;top:407px;width:150px;height:36px;border:2px solid #fff;color:#fff;font-size:14px;text-align:center;line-height:32px}
.map-area{left:581px;top:0;width:619px;height:504px;background:linear-gradient(135deg,#ececec,#dcdcdc)}
.pin{left:836px;top:68px}
.address{left:581px;top:262px;width:619px;text-align:center;font-size:40px;color:var(--green);line-height:50px}
.map-btn{left:815px;top:407px;width:150px;height:36px;background:var(--green);color:#fff;font-size:14px;text-align:center;line-height:36px}

/* footer */
.site-footer{top:3511px;height:311px;background:var(--footer);color:var(--footer-text)}
.fcol{font-size:9px;line-height:12px}
.fcol h5{font-size:11px;color:#fff;font-weight:700;margin-bottom:6px}
.newsletter{display:flex;margin-top:4px}
.newsletter span{width:95px;height:22px;background:#fff;color:#888;font-size:8px;padding:6px}
.newsletter b{width:55px;height:22px;background:var(--green);color:#fff;font-size:8px;text-align:center;line-height:22px}
.fsocial{display:flex;gap:6px;margin-top:4px}
.fsocial i{width:14px;height:14px;border-radius:50%;background:var(--green);display:block}
.footer-rule{left:296px;top:234px;width:660px;height:1px;background:#555}
.copyright{left:296px;top:268px;font-size:9px}
.footer-brand{left:550px;top:260px;width:100px;text-align:center;font-size:9px;color:#fff;font-weight:700}
</style>
</head>
<body>

<header class="site-header">
  <div class="abs brand"><div class="brand-mark"></div><div class="brand-name">Pebbledesk Writer</div></div>
  <nav class="abs main-nav"><a class="active" href="#">Home</a><a href="#">Tour</a><a href="#">Price</a><a href="#">Our Team</a><a href="#">Contact Us</a></nav>
  <div class="abs nav-divider"></div>
  <div class="abs social" style="left:834px"></div>
  <div class="abs social" style="left:867px"></div>
  <div class="abs social" style="left:900px"></div>
  <div class="abs nav-divider2"></div>
  <div class="abs login">Login</div>
  <div class="abs register">Register</div>
</header>

<section class="hero">
  <div class="abs hero-art" role="img" aria-label="Illustration of a desk with a computer monitor, mug, glasses, pen holder and mouse"></div>
  <div class="abs hero-title center">Easy, Online Mail Merge</div>
  <div class="abs hero-btn center">Start a Free Trail</div>
  <div class="abs hero-sub center">Start building your mail merge online now!</div>
  <div class="abs slider-dots"><div class="dot ring"></div><div class="dot"></div><div class="dot"></div></div>
</section>

<section class="intro-band">
  <h2>Do you have a letter you need to send out to multiple people?</h2>
  <p>Mail merge is the automatic addition of names and addresses from a spreadsheet to letters and envelopes in order to facilitate sending personalised mail to many people.</p>
</section>

<section class="features">
  <div class="abs feature" style="left:224px">
    <div class="feature-icon"><svg width="80" height="80" viewBox="0 0 80 80" fill="none" stroke="#abd037" stroke-width="4"><circle cx="40" cy="40" r="34"/><ellipse cx="40" cy="40" rx="15" ry="34"/><line x1="6" y1="40" x2="74" y2="40"/><path d="M11 23h58M11 57h58"/></svg></div>
    <h3>Easy to Use</h3><hr>
    <p>Get up and running in minutes, not hours. Satisfaction guaranteed!</p><div class="rule"></div>
  </div>
  <div class="abs feature" style="left:479px">
    <div class="feature-icon"><svg width="80" height="80" viewBox="0 0 80 80" fill="none" stroke="#abd037" stroke-width="6" stroke-linecap="round"><path d="M8 34a46 46 0 0 1 64 0"/><path d="M20 46a29 29 0 0 1 40 0"/><path d="M31 57a13 13 0 0 1 18 0"/><circle cx="40" cy="66" r="3" fill="#abd037"/></svg></div>
    <h3>Fast &amp; Reliable</h3><hr>
    <p>Our system was designed with speed in mind. No need to stress over converting your data.</p><div class="rule"></div>
  </div>
  <div class="abs feature" style="left:759px">
    <div class="feature-icon"><svg width="80" height="80" viewBox="0 0 80 80" fill="none" stroke="#abd037" stroke-width="4" stroke-linejoin="round"><path d="M40 70 10 40a17 17 0 0 1 30-24 17 17 0 0 1 30 24z"/></svg></div>
    <h3>Our Customers Love Us</h3><hr>
    <p>We have hundreds of businesses worldwide who streamline their paperwork.</p><div class="rule"></div>
  </div>
</section>

<section class="steps">
  <div class="abs steps-art" role="img" aria-label="Illustration of an office worker typing at a laptop"></div>
  <h2 class="abs">100% Easier Than Using Quillpad Docs!</h2>
  <p class="abs lead">Lorem ipsum is simply dummy text of the printing and typesetting industry.</p>
  <div class="abs step" style="top:185px"><div class="step-num">1</div><div><h4>Upload Your Data</h4><p>Create a list of addresses, names or other data</p></div></div>
  <div class="abs step" style="top:241px"><div class="step-num">2</div><div><h4>Design Your Template</h4><p>Build your document in your browser, it's easy</p></div></div>
  <div class="abs step" style="top:298px"><div class="step-num">3</div><div><h4>Merge to PDF</h4><p>Combine it all into a PDF ready for print</p></div></div>
</section>

<section class="pricing">
  <h2 class="abs center">Price The Pebbledesk Writer</h2>
  <div class="abs plan plan-free">
    <div class="plan-label">FREE ACCOUNT</div>
    <div class="plan-price">FREE</div>
    <div class="plan-detail" style="margin-top:10px"><b>1 Week Free Trial</b><br>Learn how to use<br>Pebbledesk Writer<br>Get your first week free</div>
    <div class="plan-btn">Start a Free Trail</div>
  </div>
  <div class="abs plan plan-paid">
    <div class="plan-label">PAID ACCOUNT</div>
    <div class="plan-price"><sup>$</sup>12</div>
    <div class="plan-sub">USD per month</div>
    <div class="plan-detail"><b>Unlimited</b> pages included<br><b>Unlimited</b> backgrounds<br><b>Unlimited</b> datasources<br><b>Unlimited</b> templates</div>
    <div class="plan-btn">Start a Free Trail</div>
  </div>
</section>

<section class="team">
  <h2 class="abs center">Meet The Team</h2>
  <div class="abs member" style="left:217px">
    <div class="member-photo" role="img" aria-label="Portrait photo of Tobin"></div>
    <div class="member-badge"><svg width="44" height="40" viewBox="0 0 44 40" fill="none" stroke="#fff" stroke-width="3"><rect x="3" y="3" width="28" height="20" rx="3"/><path d="M13 23v9l8-9"/><path d="M31 12h8v18h-5v6l-6-6h-8v-5"/></svg></div>
    <h3>Tobin</h3>
    <p>Our communications expert is Tobin. He's a bit shy but once you get to know him he's fiercely intelligent and ready to do his part.</p>
  </div>
  <div class="abs member" style="left:469px">
    <div class="member-photo" role="img" aria-label="Portrait photo of Emery"></div>
    <div class="member-badge"><svg width="44" height="44" viewBox="0 0 44 44" fill="none" stroke="#fff" stroke-width="3"><circle cx="22" cy="22" r="17"/><path d="M22 5v34M12 14h6M26 30h6M12 28h6M26 14h6"/></svg></div>
    <h3>Emery</h3>
    <p>The brains of this operation is no doubt Emery. He's got such a great overview, he keeps everyone in check and leaves no stone unturned.</p>
  </div>
  <div class="abs member" style="left:724px">
    <div class="member-photo" role="img" aria-label="Portrait photo of Fennick"></div>
    <div class="member-badge"><svg width="40" height="40" viewBox="0 0 40 40" fill="none" stroke="#fff" stroke-width="3"><path d="M6 12h22v16a8 8 0 0 1-8 8h-6a8 8 0 0 1-8-8z"/><path d="M28 16h4a4 4 0 0 1 0 8h-4"/></svg></div>
    <h3>Fennick</h3>
    <p>You know it's gonna be a good day when Fennick shows up. He's full of jokes and just creates the most relaxed working atmosphere.</p>
  </div>
  <div class="abs team-dots"><span></span><span class="ring"></span></div>
</section>

<section class="testimonial">
  <div class="abs avatar" role="img" aria-label="Portrait photo of customer Dana Holt"></div>
  <p class="abs kicker">See what some of our satisfied users have to say about Pebbledesk Writer</p>
  <blockquote class="abs">We were previously using a mailing house to manage our invoices. We've been able to give them the flick, saving us $2,000 a month in outsourcing printing. We can now do the while job right here from our office.</blockquote>
  <p class="abs author">DANA HOLT</p>
  <div class="abs slider-dots"><div class="dot ring"></div><div class="dot"></div><div class="dot"></div><div class="dot"></div></div>
</section>

<section class="clients">
  <h2 class="abs center">We're Making Business Easier for Everyone!</h2>
  <p class="abs center">We're passionate about making software that makes peoples lives easier. We know business is hard at times, but it<br>doesn't have to be. Here are just a few of the people we've helped.</p>
  <div class="abs client-row">
    <div class="client"><i></i>Tallow</div>
    <div class="client"><i></i>Rivetta</div>
    <div class="client"><i></i>Marlow</div>
    <div class="client"><i></i>Sunpoint</div>
    <div class="client"><i></i>Brightbite</div>
    <div class="client"><i></i>Orla Penn</div>
    <div class="client"><i></i>Kestrel</div>
  </div>
</section>

<section class="contact">
  <div class="abs contact-form">
    <h2 class="abs">Send us a message</h2><hr>
    <div class="abs field" style="top:152px">Your Name</div>
    <div class="abs field" style="top:193px">Your E-mail</div>
    <div class="abs field" style="top:234px">Your Phone</div>
    <div class="abs field message" style="top:275px">Message</div>
    <div class="abs clear">Clear <span></span></div>
    <div class="abs send-btn">Send Message</div>
  </div>
  <div class="abs map-area" role="img" aria-label="Street map showing the office location"></div>
  <svg class="abs pin" width="112" height="168" viewBox="0 0 112 168"><path d="M56 4a52 52 0 0 0-52 52c0 40 52 108 52 108s52-68 52-108A52 52 0 0 0 56 4z" fill="#abd037"/><circle cx="56" cy="56" r="20" fill="#e4e4e4"/></svg>
  <div class="abs address">Address of<br>Pebbledesk Writer</div>
  <div class="abs map-btn">View Map</div>
</section>

<footer class="site-footer">
  <div class="abs fcol" style="left:296px;top:36px"><h5>Get Started</h5>Create FREE Account<br>Login</div>
  <div class="abs fcol" style="left:296px;top:105px"><h5>Content</h5>Lorem ipsum is simply dummy<br>text of the</div>
  <div class="abs fcol" style="left:296px;top:171px"><h5>Call us</h5>1+0 000 000 0000<br>To speak with our representative</div>
  <div class="abs fcol" style="left:451px;top:36px"><h5>Link</h5>Home<br>Tour<br>Price<br>Our Team<br>Contact Us</div>
  <div class="abs fcol" style="left:451px;top:171px"><h5>Email us</h5>support@pebbledeskwriter.com</div>
  <div class="abs fcol" style="left:604px;top:36px"><h5>Email Marketing Blog</h5>Lorem ipsum is simply dummy text of the...<br>Lorem ipsum is simply dummy text of the...<br>Lorem ipsum is simply dummy text of the...<br>Lorem ipsum is simply dummy text of the...<br>Lorem ipsum is simply dummy text of the...</div>
  <div class="abs fcol" style="left:604px;top:171px"><h5>Join 20,000+ Newsletter Readers</h5><div class="newsletter"><span>Your Name</span><b>Subscribe</b></div></div>
  <div class="abs fcol" style="left:810px;top:36px"><h5>Tour</h5>What is Mail Merge<br>What Can It Make<br>Who Is It For<br>Merging Paperwork<br>Screenshots</div>
  <div class="abs fcol" style="left:810px;top:171px"><h5>Let's connect</h5><div class="fsocial"><i></i><i></i><i></i></div></div>
  <div class="abs footer-rule"></div>
  <div class="abs copyright">© Copyright 2017 Hollin Technologies. All Rights Reserved</div>
  <div class="abs footer-brand">Pebbledesk</div>
</footer>

</body>
</html>
```